Website for UK Fintech Company specialising in Auto-Finance asset management

We need a website for a FINTECH business called KELVO Asset Management. We have developed and licenced an innovative platform to provide financial institutions whom provide secured Asset finance loans to consumer and commercial clients, allowing for real time tracking and management of defaulted accounts pending repossession. The KELVO Asset Management platform is a total recoveries solution through the cycle, from the moment the lender has to recover the vehicle (due to default/non-payment) to the disposal of the vehicle (via sale at Motor Auctions or by selling to a Car dealership network). The data provided from external services allows the Financier to make informed decisions, such as whether it is economical to continue the recovery and decide which sales channel is better suited for their assets to maximise residual values and minimise financial losses. The KELVO platform provides an array of MI reporting and uses a systematic approach utilising exception reporting to identify key areas of non-performance to enable focus where needed. KELVO also provides a leading Debt collection service recovering end-of-cycle losses such as Financial Shortfall and losses in vehicle values due to conditions and excessive damage.

We also require a new logo for out new product called PL-Certify

Target Market(s)

Financial institutions whom provide secured Asset finance loans to consumer and commercial clients

Industry/Entity Type

Financial Service

Logo Text

PL- Certify (this is for a new product which forms part of the KELVO Asset Mangement Platform

Number of Pages Required

4 page

Font styles to use
Serif
Sans Serif

Colors

Designer to choose colors to be used in the design.

Requirements
Must have
• We need a simple website with a broken down as follows;
• • Landing page
• • Services page
• • About us page
• • KELVO Asset Management Platform login page (client facing)
Nice to have
• Our slogan is 'Auto-Finance Expertise'
• We are very much open to suggestions as long as we can create a professional/ corporate / modern feel to the website. We are a FINTECH company, and that needs to come across
Should not have
• Whilst we are an asset management company primarily managing vehicles through our platform, we don't want it to look like a car dealership website!:)

```html
<!DOCTYPE html>
<html lang="en">
<head>
<meta charset="utf-8">
<title>KELVO Asset Management – Services</title>
<link href="https://fonts.googleapis.com/css2?family=Open+Sans:wght@300;400;600;700;800&display=swap" rel="stylesheet">
<style>
  :root{
    --orange:#f07d00;
    --orange-soft:rgba(240,125,0,.85);
    --text:#444;
    --muted:#666;
    --heading:#555;
    --ink:#222;
    --white:#fff;
    --hero-a:#6d7278;
    --hero-b:#c9ccd0;
    --hero-c:#e9eaec;
  }
  *{box-sizing:border-box;margin:0;padding:0}
  html,body{width:768px;height:1200px;overflow:hidden;background:var(--white)}
  body{position:relative;font-family:"Open Sans",Arial,sans-serif;color:var(--text)}

  .top-rule{position:absolute;left:0;top:0;width:768px;height:3px;background:var(--orange)}

  .site-header{position:absolute;left:0;top:3px;width:768px;height:86px}
  .brand-name{position:absolute;font-weight:700;line-height:1;color:var(--ink)}
  .site-header .brand-name{left:64px;top:26px;font-size:32px}
  .contact{position:absolute;left:476px;top:11px;display:flex;align-items:center;gap:3px;font-size:12px;color:#777}
  .call-btn{position:absolute;left:647px;top:11px;width:57px;height:16px;background:var(--orange);color:var(--white);font-size:7px;font-weight:600;display:flex;align-items:center;justify-content:center}
  .main-nav{position:absolute;top:43px;left:0;width:768px;font-size:12px;color:#444}
  .main-nav a{position:absolute;color:inherit;text-decoration:none;padding-bottom:4px}
  .main-nav a.active{border-bottom:2px solid var(--orange)}
  .main-nav .login{display:flex;align-items:center;gap:3px}

  .hero{position:absolute;left:0;top:89px;width:768px;height:267px;background:linear-gradient(120deg,var(--hero-a) 0%,var(--hero-b) 45%,var(--hero-c) 100%)}
  .hero-title{position:absolute;left:0;top:81px;width:326px;height:30px;background:var(--orange-soft);color:var(--white);font-size:18px;font-weight:400;padding-left:65px;line-height:30px}
  .hero-copy{position:absolute;left:0;top:133px;width:420px;height:49px;background:rgba(240,140,40,.45);color:var(--white);font-size:9.6px;line-height:11.6px;padding:5px 20px 0 65px}

  .section-title{position:absolute;top:388px;left:0;width:768px;text-align:center;font-size:25px;font-weight:400;color:var(--heading)}

  .service-grid{position:absolute;left:74px;top:460px;display:grid;grid-template-columns:166px 170px 167px 150px;grid-auto-rows:322px}
  .service{position:relative}
  .service h3{font-size:11.5px;font-weight:700;color:#444;line-height:13.5px;height:44px;padding-left:2px}
  .service p{font-size:8.2px;line-height:10.4px;color:var(--muted);width:118px;height:63px;margin-top:5px}
  .service .more{display:inline-block;margin-top:20px;font-size:12px;color:#555;text-decoration:none;border-bottom:1px solid #999;line-height:13px}
  .service svg{position:absolute;left:28px;top:180px;width:56px;height:66px}

  .cta{position:absolute;left:253px;top:1086px;width:262px;height:26px;border-radius:5px;background:var(--orange);color:var(--white);font-size:16px;font-weight:700;letter-spacing:.4px;display:flex;align-items:center;justify-content:center;text-decoration:none}

  .site-footer{position:absolute;left:0;top:1158px;width:768px;height:30px}
  .site-footer .brand-name{left:92px;top:4px;font-size:17px}
  .copyright{position:absolute;left:297px;top:12px;font-size:9.5px;color:#555}
  .social{position:absolute;left:567px;top:10px;display:flex;gap:7px}
  .social span{width:16px;height:16px;border:1.3px solid var(--orange);border-radius:50%}
</style>
</head>
<body>
  <div class="top-rule"></div>

  <header class="site-header">
    <div class="brand-name">KELVO</div>
    <div class="contact">
      <svg width="16" height="16" viewBox="0 0 16 16" aria-hidden="true"><circle cx="8" cy="8" r="7" fill="none" stroke="#f07d00" stroke-width="1.4"/><rect x="4" y="5" width="8" height="6" fill="none" stroke="#f07d00"/><path d="M4 5l4 3.5L12 5" fill="none" stroke="#f07d00"/></svg>
      email@kelvomail.com
    </div>
    <div class="call-btn">Call Us</div>
    <nav class="main-nav">
      <a href="#" style="left:393px">Home</a>
      <a href="#" style="left:479px">About Us</a>
      <a href="#" class="active" style="left:565px">Services</a>
      <a href="#" class="login" style="left:652px">Login
        <svg width="11" height="11" viewBox="0 0 11 11" aria-hidden="true"><circle cx="5.5" cy="3" r="2.6" fill="#111"/><path d="M0.5 11c0-3.5 2.2-5 5-5s5 1.5 5 5z" fill="#111"/></svg>
      </a>
    </nav>
  </header>

  <section class="hero" role="img" aria-label="Photograph of business people's hands reviewing documents at a meeting table">
    <h1 class="hero-title">WELCOME TO KELVO</h1>
    <p class="hero-copy">Lorem ipsum dolor sit amet, amet feugiat lacus, pretium imperdiet, consectetuer rutrum dui et, quam vitae accumsan eleifend mattis adipiscing duis.</p>
  </section>

  <h2 class="section-title">Our Services</h2>

  <main class="service-grid">
    <article class="service">
      <h3>Licensing</h3>
      <p>Lorem ipsum dolor sit amet, amet feugiat lacus, pretium imperdiet, consectetuer rutrum dui et, quam vitae accumsan eleifend mattis adipiscing duis.</p>
      <a class="more" href="#">Learn More</a>
      <svg viewBox="0 0 56 66" aria-hidden="true"><rect x="4" y="2" width="46" height="58" rx="3" fill="none" stroke="#f07d00" stroke-width="4"/><path d="M13 14h26M13 22h26M13 30h18" stroke="#f07d00" stroke-width="4"/><circle cx="18" cy="44" r="7" fill="#fff" stroke="#f07d00" stroke-width="4"/><path d="M12 50v14l6-4 6 4V50" fill="#f07d00"/></svg>
    </article>
    <article class="service">
      <h3>Assess Management Platform</h3>
      <p>Lorem ipsum dolor sit amet, amet feugiat lacus, pretium imperdiet, consectetuer rutrum dui et, quam vitae accumsan eleifend mattis adipiscing duis.</p>
      <a class="more" href="#">Learn More</a>
      <svg viewBox="0 0 56 66" aria-hidden="true"><circle cx="28" cy="20" r="13" fill="none" stroke="#f07d00" stroke-width="8" stroke-dasharray="6 4.2"/><circle cx="28" cy="20" r="10" fill="none" stroke="#f07d00" stroke-width="4"/><path d="M2 46c8-6 16-6 24-2h12c3 0 3 5 0 5H26l14 0 14-8c2 0 3 2 1 4L38 58H2z" fill="#f07d00"/></svg>
    </article>
    <article class="service">
      <h3>MI Reporting</h3>
      <p>Lorem ipsum dolor sit amet, amet feugiat lacus, pretium imperdiet, consectetuer rutrum dui et, quam vitae accumsan eleifend mattis adipiscing duis.</p>
      <a class="more" href="#">Learn More</a>
      <svg viewBox="0 0 56 66" aria-hidden="true"><circle cx="28" cy="32" r="26" fill="#f07d00"/><path d="M15 21v24h27" fill="none" stroke="#fff" stroke-width="2.5"/><rect x="19" y="32" width="4" height="11" fill="#fff"/><rect x="25" y="27" width="4" height="16" fill="#fff"/><rect x="31" y="30" width="4" height="13" fill="#fff"/><rect x="37" y="24" width="4" height="19" fill="#fff"/></svg>
    </article>
    <article class="service">
      <h3>Collection</h3>
      <p>Lorem ipsum dolor sit amet, amet feugiat lacus, pretium imperdiet, consectetuer rutrum dui et, quam vitae accumsan eleifend mattis adipiscing duis.</p>
      <a class="more" href="#">Learn More</a>
      <svg viewBox="0 0 56 66" aria-hidden="true"><rect x="12" y="8" width="26" height="10" rx="2" fill="#f07d00"/><rect x="12" y="20" width="26" height="10" rx="2" fill="#f07d00"/><rect x="12" y="32" width="26" height="10" rx="2" fill="#f07d00"/><path d="M6 52c6-6 14-8 22-4h8M6 58c10 6 24 6 38 0" fill="none" stroke="#f07d00" stroke-width="4"/><rect x="46" y="46" width="6" height="16" fill="#f07d00"/></svg>
    </article>

    <article class="service">
      <h3>Licensing</h3>
      <p>Lorem ipsum dolor sit amet, amet feugiat lacus, pretium imperdiet, consectetuer rutrum dui et, quam vitae accumsan eleifend mattis adipiscing duis.</p>
      <a class="more" href="#">Learn More</a>
      <svg viewBox="0 0 56 66" aria-hidden="true"><rect x="4" y="2" width="46" height="58" rx="3" fill="none" stroke="#f07d00" stroke-width="4"/><path d="M13 14h26M13 22h26M13 30h18" stroke="#f07d00" stroke-width="4"/><circle cx="18" cy="44" r="7" fill="#fff" stroke="#f07d00" stroke-width="4"/><path d="M12 50v14l6-4 6 4V50" fill="#f07d00"/></svg>
    </article>
    <article class="service">
      <h3>Assess Management Platform</h3>
      <p>Lorem ipsum dolor sit amet, amet feugiat lacus, pretium imperdiet, consectetuer rutrum dui et, quam vitae accumsan eleifend mattis adipiscing duis.</p>
      <a class="more" href="#">Learn More</a>
      <svg viewBox="0 0 56 66" aria-hidden="true"><circle cx="28" cy="20" r="13" fill="none" stroke="#f07d00" stroke-width="8" stroke-dasharray="6 4.2"/><circle cx="28" cy="20" r="10" fill="none" stroke="#f07d00" stroke-width="4"/><path d="M2 46c8-6 16-6 24-2h12c3 0 3 5 0 5H26l14 0 14-8c2 0 3 2 1 4L38 58H2z" fill="#f07d00"/></svg>
    </article>
    <article class="service">
      <h3>MI Reporting</h3>
      <p>Lorem ipsum dolor sit amet, amet feugiat lacus, pretium imperdiet, consectetuer rutrum dui et, quam vitae accumsan eleifend mattis adipiscing duis.</p>
      <a class="more" href="#">Learn More</a>
      <svg viewBox="0 0 56 66" aria-hidden="true"><circle cx="28" cy="32" r="26" fill="#f07d00"/><path d="M15 21v24h27" fill="none" stroke="#fff" stroke-width="2.5"/><rect x="19" y="32" width="4" height="11" fill="#fff"/><rect x="25" y="27" width="4" height="16" fill="#fff"/><rect x="31" y="30" width="4" height="13" fill="#fff"/><rect x="37" y="24" width="4" height="19" fill="#fff"/></svg>
    </article>
    <article class="service">
      <h3>Collection</h3>
      <p>Lorem ipsum dolor sit amet, amet feugiat lacus, pretium imperdiet, consectetuer rutrum dui et, quam vitae accumsan eleifend mattis adipiscing duis.</p>
      <a class="more" href="#">Learn More</a>
      <svg viewBox="0 0 56 66" aria-hidden="true"><rect x="12" y="8" width="26" height="10" rx="2" fill="#f07d00"/><rect x="12" y="20" width="26" height="10" rx="2" fill="#f07d00"/><rect x="12" y="32" width="26" height="10" rx="2" fill="#f07d00"/><path d="M6 52c6-6 14-8 22-4h8M6 58c10 6 24 6 38 0" fill="none" stroke="#f07d00" stroke-width="4"/><rect x="46" y="46" width="6" height="16" fill="#f07d00"/></svg>
    </article>
  </main>

  <a class="cta" href="#">BOOK A FREE CONSULTATION</a>

  <footer class="site-footer">
    <div class="brand-name">KELVO</div>
    <p class="copyright">Copyright © 2018. All Rights Reserved</p>
    <div class="social" aria-label="Social links">
      <span></span><span></span><span></span><span></span><span></span>
    </div>
  </footer>
</body>
</html>
```